Web Design Project

We are building a site on Wordpress that will sell signed posters from various popular music artists - the name of the site is The Harlow Lane Studio. Consumers will be able to select from a list of personal messages and once they purchase, receive a high quality unique poster from the artist with a rendered handwriting based on the artist agreement.
We don't want anything too complicated, but would prefer a modern clean aesthetic. This is an e-commerce site, and will include a basic shopping cart. The artist galleries will be straightforward and may include some branding in the artist's look and feel.
Some sites to consider: kelvo.com, brimwexhall.com, quorble.com - but we would like it a bit cleaner and less busy.
Reason: I will be accepting designs up until Sunday evening EST. Thank you!
Reason: Thank you for your submissions! The client is reviewing the submissions and needs to run this by management before we select.
Reason: We are still delayed on the client's end as they are doing some logo and color re-designs.
Thanks for your patience.
Reason: We are trying to confirm a design choice with the client. Apologies for the delay!

```html
<!DOCTYPE html>
<html lang="en">
<head>
<meta charset="utf-8">
<title>The Harlow Lane Studio – Signed Music Posters</title>
<link rel="stylesheet" href="https://fonts.googleapis.com/css2?family=Arimo:wght@400;700&family=Oswald:wght@500;700&family=Fjalla+One&display=swap">
<style>
:root{
  --red:#d9262b;
  --red-dark:#a9161b;
  --teal:#23908e;
  --teal-dark:#17706f;
  --yellow:#f7d21c;
  --ink:#222;
  --text:#555;
  --muted:#888;
  --line:#dedede;
  --panel:#efefef;
  --header:#ececec;
  --footer:#393939;
  --footer-deep:#2b2b2b;
  --footer-head:#4fb3bf;
  --white:#fff;
}
*{box-sizing:border-box;margin:0;padding:0}
html,body{width:1141px;height:1200px;overflow:hidden}
body{position:relative;background:var(--white);font-family:"Arimo",Arial,sans-serif;color:var(--text);font-size:11px}
.abs{position:absolute}
a{color:inherit;text-decoration:none}
ul{list-style:none}

/* header */
.site-header{left:142px;top:0;width:860px;height:102px;background:var(--header)}
.site-header::after{content:"";position:absolute;left:0;right:0;bottom:-5px;height:6px;
  background:radial-gradient(circle at 4px 0,var(--header) 4px,transparent 4.5px) 0 0/8px 6px repeat-x}
.brand{left:170px;top:24px}
.brand-name{font-family:"Oswald",sans-serif;font-weight:700;font-size:34px;line-height:1;color:var(--red);letter-spacing:-.5px;text-transform:uppercase}
.brand-tag{font-family:"Arimo",sans-serif;font-weight:700;font-size:10px;color:var(--ink);margin-top:4px;letter-spacing:.2px;text-transform:uppercase}
.account-links{left:668px;top:21px;font-size:11px;color:#666}
.cart{left:828px;top:15px;width:150px;height:24px;background:#fafafa;border:1px solid #ddd;border-radius:3px;font-size:11px;color:#333;padding:5px 0 0 26px}
.cart svg{position:absolute;left:7px;top:5px}
.cart .go{position:absolute;right:4px;top:3px;background:var(--teal);color:#fff;font-weight:700;font-size:9px;padding:3px 5px;border-radius:2px}
.search{left:649px;top:52px;width:329px;height:30px;display:flex}
.search .field{flex:1;background:#fff;border:1px solid #ddd;color:#aaa;font-size:12px;padding:7px 0 0 26px;position:relative}
.search .field svg{position:absolute;left:8px;top:8px}
.search .btn{width:92px;background:var(--red);color:#fff;font-weight:700;font-size:12px;text-align:center;padding-top:8px}

/* navigation */
.nav-ribbon{left:117px;top:120px;width:905px;height:46px}
.main-nav{left:142px;top:122px;width:856px;height:41px;background:linear-gradient(#e23137,#c81e24);display:flex;align-items:center}
.main-nav a{font-family:"Fjalla One",sans-serif;color:#fff;font-size:15px;text-transform:uppercase;letter-spacing:.4px;position:absolute;top:11px}
.main-nav a.current{background:var(--yellow);color:var(--red);padding:1px 8px;top:9px}

/* categories */
.categories{left:139px;top:179px;width:176px;height:261px;background:linear-gradient(90deg,#fff 70%,#f0f0f0)}
.tab{background:var(--teal);color:#fff;font-size:14px;height:28px;padding:5px 0 0 12px;position:relative}
.tab::after{content:"";position:absolute;right:-12px;top:0;border-left:12px solid var(--teal);border-top:14px solid transparent;border-bottom:14px solid transparent}
.categories .tab{width:170px}
.categories ul{padding:10px 0 0 10px}
.categories li{font-size:11.5px;color:#444;height:21.7px;padding-left:14px;position:relative}
.categories li::before{content:"»";position:absolute;left:0;top:-1px;color:#777}
.categories li.hot::before{color:var(--red)}

/* slider */
.slider{left:318px;top:179px;width:484px;height:261px;background:linear-gradient(135deg,#2c9c99,#1c7d7c);overflow:hidden}
.slider-photo{position:absolute;right:4px;top:8px;width:310px;height:210px;background:linear-gradient(120deg,#e0a060 0%,#c4682d 45%,#3a2a22 100%);clip-path:polygon(8% 0,100% 0,100% 100%,0 100%)}
.slider-title{position:absolute;left:45px;top:96px;font-family:"Fjalla One",sans-serif;color:#fff;font-size:25px;line-height:1.2}
.shop-now{position:absolute;right:20px;top:204px;background:var(--red);color:#fff;font-weight:700;font-size:11px;padding:6px 14px;text-transform:uppercase}
.slide-arrow{position:absolute;top:105px;width:28px;height:28px;border-radius:50%;background:#2a2a2a}
.slide-arrow svg{position:absolute;left:9px;top:8px}
.dots{left:530px;top:424px;display:flex;gap:9px}
.dots span{width:11px;height:11px;border-radius:50%;background:#fff;border:1px solid #ccc}
.dots span.on{background:var(--red);border-color:var(--red)}

/* newsletter */
.newsletter{left:813px;top:179px;width:188px;height:127px;background:var(--teal);color:#fff;padding:8px 8px}
.newsletter h3{font-weight:400;font-size:14px}
.newsletter p{font-size:9.5px;line-height:1.25;margin-top:5px;color:#e5f4f3}
.newsletter .email{margin-top:8px;height:22px;background:#fff;color:#666;font-size:10px;padding:5px 0 0 24px;position:relative}
.newsletter .email svg{position:absolute;left:7px;top:7px}
.newsletter .submit{position:absolute;right:14px;bottom:10px;background:var(--red);font-weight:700;font-size:10px;padding:4px 10px}
.learn-more{left:813px;top:319px;width:188px;height:121px;background:linear-gradient(#f6f6f6,#e6e6e6);border:1px solid #ddd;padding:14px 0 0 16px}
.learn-more .big{font-family:"Oswald",sans-serif;font-weight:700;font-size:20px;color:var(--red);line-height:1}
.learn-more .sub{font-weight:700;font-size:11.5px;color:#333;margin-top:5px}
.learn-more .sub2{font-weight:700;font-size:11.5px;color:var(--teal);margin-top:3px}

/* recent posters */
.section-title{font-family:"Arimo",sans-serif;color:var(--red);font-size:16px}
.recent-title{left:142px;top:472px}
.view-all{background:var(--red);color:#fff;font-size:9px;font-weight:700;padding:2px 7px;margin-left:8px;vertical-align:2px;text-transform:uppercase}
.recent-rule{left:142px;top:500px;width:652px;height:1px;background:var(--line)}
.poster{top:518px;width:158px;text-align:center}
.poster .art{height:134px}
.poster h4{font-size:13px;color:#222;margin-top:16px}
.poster .meta{font-size:10px;color:var(--muted);margin-top:2px}
.poster .price{font-size:19px;color:#333;margin-top:6px}
.poster .add{display:inline-block;margin-top:7px;background:var(--teal);color:#fff;font-size:10px;padding:3px 9px}
.poster .add svg{vertical-align:-1px;margin-right:3px}

/* connect & feed */
.connect{left:848px;top:481px;width:159px;height:26px;background:var(--teal);color:#fff;font-size:13px;text-align:center;padding-top:5px}
.connect::before{content:"";position:absolute;left:-12px;top:0;border-right:12px solid var(--teal);border-top:13px solid transparent;border-bottom:13px solid transparent}
.social{left:822px;top:515px;display:flex;gap:7px}
.social span{width:23px;height:23px;border-radius:4px}
.feed{left:813px;top:574px;width:188px;height:254px;background:#f4f4f4;border:1px solid #ccc}
.feed-head{height:40px;background:linear-gradient(#8a8a8a,#6d6d6d);color:#fff;padding:5px 0 0 42px;position:relative}
.feed-head .sq{position:absolute;left:9px;top:8px;width:24px;height:24px;background:#fff;border-radius:3px}
.feed-head small{font-size:9px;display:block;color:#e8e8e8}
.feed-head b{font-size:13px}
.tweet{position:relative;padding:6px 6px 6px 36px;border-bottom:1px solid #ddd;background:#fff;font-size:9.5px;line-height:1.3;color:#555;height:70px;overflow:hidden}
.tweet .av{position:absolute;left:8px;top:8px;width:20px;height:20px;background:#b6c7cf}
.tweet b{color:var(--teal)}
.tweet .when{color:#999;font-size:8.5px}
.feed-foot{position:absolute;left:0;right:0;bottom:0;height:30px;background:#6f6f6f;color:#fff;font-size:10px;padding:8px 0 0 12px}
.feed-foot b{margin-right:14px}

/* content blocks */
.block-title{top:765px;font-size:15px;color:var(--red)}
.block-title svg{vertical-align:-1px;margin-right:5px}
.block{top:790px;height:163px;background:var(--panel)}
.spot-photo{left:155px;top:820px;width:90px;height:109px;background:linear-gradient(160deg,#d8c9c4,#8c6a70 60%,#3d3035)}
.spot-text{left:258px;top:818px;width:88px}
.spot-text h4{font-size:13px;color:#222}
.spot-text p{font-size:10px;line-height:1.3;margin-top:5px;color:#666}
.btn-teal{background:var(--teal);color:#fff;font-weight:700;font-size:9.5px;padding:4px 8px;text-transform:uppercase}
.news{left:375px;top:815px;width:195px}
.news .item{background:#fff;padding:0;margin-bottom:12px;background:none}
.news h5{font-size:11px;line-height:1.35;color:#333}
.news .by{font-size:10px;color:#888;margin-top:3px}
.news-rule{left:375px;top:869px;width:190px;height:1px;background:var(--line)}
.event-date{left:597px;top:818px;width:39px;height:42px;background:var(--teal);color:#fff;text-align:center}
.event-date b{display:block;font-family:"Oswald",sans-serif;font-size:21px;line-height:1.2;font-weight:500}
.event-date span{display:block;background:#fff;color:#555;font-size:9px;margin:0 2px;line-height:12px}
.event-text{left:645px;top:818px;width:145px}
.event-text h4{font-size:12.5px;color:#222;line-height:1.25}
.event-text .place{font-size:9.5px;color:#888;margin-top:6px}
.event-desc{left:600px;top:880px;width:190px;font-size:10px;line-height:1.35;color:#666}

/* footer */
.site-footer{left:0;top:986px;width:1141px;height:214px;background:var(--footer)}
.phone-box{left:142px;top:986px;width:184px;height:214px;background:var(--footer-deep);padding:24px 0 0 24px;color:#cfcfcf}
.foot-head{font-family:"Arimo",sans-serif;font-weight:700;font-size:13px;color:var(--footer-head);text-transform:uppercase;letter-spacing:.3px}
.phone-box .num{font-size:21px;color:#fff;font-weight:700;margin-top:10px}
.phone-box p{font-size:10px;line-height:1.6;margin-top:6px}
.foot-col{top:1010px;color:#cfcfcf;font-size:11px}
.foot-col ul{margin-top:10px}
.foot-col li{height:19.5px}
.foot-col.uploads li::before{content:"» ";color:var(--footer-head)}
.pay{left:810px;top:1040px;width:160px;display:grid;grid-template-columns:repeat(4,31px);gap:6px 8px}
.pay span{height:19px;background:#eef0f2;border-radius:2px}
.copyright{left:813px;top:1099px;font-size:10px;color:#bbb}
</style>
</head>
<body>

<header class="abs site-header"></header>
<div class="abs brand">
  <div class="brand-name">The Harlow Lane Studio</div>
  <div class="brand-tag">Posters from various popular music artists</div>
</div>
<div class="abs account-links">Account : Customer Services</div>
<div class="abs cart">
  <svg width="14" height="12" viewBox="0 0 14 12"><path d="M0 1h3l2 7h7l2-5H4" fill="none" stroke="#444" stroke-width="1.4"/><circle cx="6" cy="10.5" r="1.2" fill="#444"/><circle cx="11" cy="10.5" r="1.2" fill="#444"/></svg>
  <b>2 items</b> in cart <span class="go">GO</span>
</div>
<div class="abs search">
  <div class="field"><svg width="12" height="12" viewBox="0 0 12 12"><circle cx="5" cy="5" r="3.8" fill="none" stroke="#999" stroke-width="1.5"/><path d="M8 8l3.5 3.5" stroke="#999" stroke-width="1.6"/></svg>Search Posters of Music Artist</div>
  <div class="btn">SEARCH</div>
</div>

<svg class="abs nav-ribbon" viewBox="0 0 905 46" aria-hidden="true">
  <polygon points="0,2 28,2 28,46 0,46 10,24" fill="var(--red-dark)"/>
  <polygon points="905,2 877,2 877,46 905,46 895,24" fill="var(--red-dark)"/>
</svg>
<nav class="abs main-nav">
  <a class="current" style="left:14px">Home</a>
  <a style="left:105px">Artist Gallery</a>
  <a style="left:272px">Signatures</a>
  <a style="left:412px">Blog</a>
  <a style="left:516px">Best Sellers</a>
  <a style="left:660px">Press</a>
  <a style="left:758px">Contact</a>
</nav>

<aside class="abs categories">
  <div class="tab">Top Categories</div>
  <ul>
    <li>Ashdown, Miriam</li>
    <li>Belcourt, Hugo</li>
    <li>Corrin, Lyle</li>
    <li class="hot">Dennet, Oswin</li>
    <li>Farrow, Idris</li>
    <li>Galbraith, Noel</li>
    <li>Hensley, Tobin</li>
    <li>Imbery, Rhea</li>
    <li>Jarrell, Wade</li>
    <li>Kestrel, Anya</li>
  </ul>
</aside>

<section class="abs slider">
  <div class="slider-photo" role="img" aria-label="Photo of a rock band posing against a warm orange backdrop"></div>
  <div class="slider-title">Posters<br>form the<br>hotterst<br>music artist</div>
  <div class="shop-now">Shop Now</div>
  <div class="slide-arrow" style="left:10px"><svg width="10" height="12" viewBox="0 0 10 12"><path d="M8 1L2 6l6 5z" fill="#fff"/></svg></div>
  <div class="slide-arrow" style="right:10px"><svg width="10" height="12" viewBox="0 0 10 12"><path d="M2 1l6 5-6 5z" fill="#fff"/></svg></div>
</section>
<div class="abs dots"><span class="on"></span><span></span><span></span><span></span></div>

<section class="abs newsletter">
  <h3>Signup for newsltter</h3>
  <p>Sign up to recive special offers, and product discount from us.</p>
  <div class="email"><svg width="11" height="8" viewBox="0 0 11 8"><rect x=".5" y=".5" width="10" height="7" fill="none" stroke="#888"/><path d="M.5.5l5 4 5-4" fill="none" stroke="#888"/></svg>Enter email</div>
  <div class="submit">SUBMIT</div>
</section>
<section class="abs learn-more">
  <div class="big">LEARN MORE</div>
  <div class="sub">About Our Proprietary</div>
  <div class="sub2">Signature Technology!</div>
</section>

<h2 class="abs section-title recent-title">Most Recent Posters <span class="view-all">View All</span></h2>
<div class="abs recent-rule"></div>

<article class="abs poster" style="left:142px">
  <div class="art" role="img" aria-label="Colourful psychedelic poster of a guitarist" style="background:linear-gradient(135deg,#e23b8a,#1b1b1b 45%,#f2b21e 75%,#2aa0d8)"></div>
  <h4>Rory Vantage</h4><div class="meta">Art Print - 16 x 16</div><div class="price">$12.99</div>
  <span class="add"><svg width="9" height="8" viewBox="0 0 9 8"><path d="M0 1h2l1 4h5l1-3H2.5" fill="none" stroke="#fff"/></svg>Add to Cart</span>
</article>
<article class="abs poster" style="left:308px">
  <div class="art" role="img" aria-label="Black and white portrait poster with signature" style="background:linear-gradient(135deg,#111,#6a6a6a 50%,#222)"></div>
  <h4>Rory Vantage</h4><div class="meta">Art Print - 16 x 16</div><div class="price">$12.99</div>
  <span class="add"><svg width="9" height="8" viewBox="0 0 9 8"><path d="M0 1h2l1 4h5l1-3H2.5" fill="none" stroke="#fff"/></svg>Add to Cart</span>
</article>
<article class="abs poster" style="left:476px">
  <div class="art" role="img" aria-label="Grey festival poster with bird and guitar artwork" style="background:linear-gradient(135deg,#b5b5b5,#8d8d8d 60%,#d8d8d8)"></div>
  <h4>Rory Vantage</h4><div class="meta">Art Print - 16 x 16</div><div class="price">$12.99</div>
  <span class="add"><svg width="9" height="8" viewBox="0 0 9 8"><path d="M0 1h2l1 4h5l1-3H2.5" fill="none" stroke="#fff"/></svg>Add to Cart</span>
</article>
<article class="abs poster" style="left:644px">
  <div class="art" role="img" aria-label="Sepia wall of graffiti writing poster" style="background:linear-gradient(135deg,#d9cbb0,#8a7a62 55%,#4a3f33)"></div>
  <h4>Rory Vantage</h4><div class="meta">Art Print - 16 x 16</div><div class="price">$12.99</div>
  <span class="add"><svg width="9" height="8" viewBox="0 0 9 8"><path d="M0 1h2l1 4h5l1-3H2.5" fill="none" stroke="#fff"/></svg>Add to Cart</span>
</article>

<div class="abs connect">Conntct With Us</div>
<div class="abs social">
  <span style="background:#4aa8dc"></span><span style="background:#3b5c98"></span><span style="background:#2a78b0"></span><span style="background:#f08a1d"></span><span style="background:#2fb4e6"></span><span style="background:#7b2c96"></span>
</div>

<aside class="abs feed">
  <div class="feed-head"><span class="sq"></span><small>What Being Said About</small><b>THLS</b></div>
  <div class="tweet"><span class="av"></span><b>THLS</b> Forgiveness rovides us freedom and releases us from the bondage of anger and the sickness that accompanies it... <b>hl.st/Q7yC3B</b><br><span class="when">yesterday · reply · retweet · fav</span></div>
  <div class="tweet"><span class="av"></span><b>THLS</b> Forgiveness ovides us freedom and releases us from the bondage of anger and the sees it.... <b>hl.st/Q7yC3B</b><br><span class="when">11 hours ago · reply · retweet · fav</span></div>
  <div class="tweet" style="height:40px"><span class="av"></span><b>THLS</b> Forgiveness ovides us freedom and releases us</div>
  <div class="feed-foot"><b>Social feed</b>Join the conversation</div>
</aside>

<h3 class="abs block-title" style="left:140px"><svg width="11" height="11" viewBox="0 0 12 12"><path d="M6 0l1.8 4H12L8.6 6.6 10 11 6 8.4 2 11l1.4-4.4L0 4h4.2z" fill="var(--red)"/></svg>Artist Spotlight</h3>
<h3 class="abs block-title" style="left:365px"><svg width="11" height="11" viewBox="0 0 11 11"><path d="M1 0v11M1 1h9l-2 3 2 3H1" fill="var(--red)" stroke="var(--red)"/></svg>News and Blog</h3>
<h3 class="abs block-title" style="left:590px"><svg width="11" height="11" viewBox="0 0 11 11"><rect x=".5" y="1.5" width="10" height="9" fill="none" stroke="var(--red)"/><path d="M.5 4h10" stroke="var(--red)" stroke-width="1.5"/></svg>Upcoming Events</h3>

<section class="abs block" style="left:142px;width:212px"></section>
<div class="abs spot-photo" role="img" aria-label="Photo of the featured pop singer on stage"></div>
<div class="abs spot-text">
  <h4>Lila Marrow</h4>
  <p>Lila Marrow came to prominence as a recording artist following the release of...</p>
</div>
<span class="abs btn-teal" style="left:261px;top:913px">More Details</span>

<section class="abs block" style="left:365px;width:212px"></section>
<div class="abs news">
  <div class="item"><h5>Check out the art we're digging right now and what's on...</h5><div class="by">Posted by: Admin</div></div>
  <div class="item" style="margin-top:22px"><h5>Check out the art we're digging right now and what's on...</h5><div class="by">Posted by: Admin</div></div>
</div>
<div class="abs news-rule"></div>
<span class="abs" style="left:518px;top:915px;color:var(--red);font-weight:700;font-size:10px">View All</span>

<section class="abs block" style="left:590px;width:212px"></section>
<div class="abs event-date"><b>26</b><span>JAN</span></div>
<div class="abs event-text">
  <h4>Concert for The Copper Saints!</h4>
  <div class="place">Ashford Hall, Union Square</div>
</div>
<div class="abs event-desc">THLS will be the apparel sponsor at the 4th Annual Bright Futures Mentors...</div>
<span class="abs btn-teal" style="left:600px;top:913px">View Details</span>

<footer class="abs site-footer"></footer>
<div class="abs phone-box">
  <div class="foot-head">Order by phone</div>
  <div class="num">01632 960 418</div>
  <p>Monday to Friday<br>9.00am-5.00pm UK time<br>contact@harlowlanestudio.com</p>
</div>
<div class="abs foot-col uploads" style="left:372px">
  <div class="foot-head">Latest uploads:</div>
  <ul><li>I Wait</li><li>It Won't be Long</li><li>I See The Stars</li><li>All I Dream</li><li>Hallelujah</li><li>Epilogue</li></ul>
</div>
<div class="abs foot-col" style="left:563px">
  <div class="foot-head">Company information</div>
  <ul style="float:left;width:92px"><li>Home</li><li>Artist Gallery</li><li>Signatures</li><li>Blog</li><li>Frames</li><li>Press</li><li>Contact</li></ul>
  <ul style="float:left"><li>FAQs</li><li>Privacy Policy</li><li>Terms of Use &amp; Legal</li><li>Store Policy</li><li>Site Map</li></ul>
</div>
<div class="abs foot-col" style="left:810px">
  <div class="foot-head">We accept payment by</div>
</div>
<div class="abs pay"><span></span><span></span><span></span><span></span><span></span><span></span><span></span><span></span></div>
<div class="abs copyright">©Copyright 2012 TheHarlowLaneStudio.com</div>

</body>
</html>
```